Tarvik Plans - Worpress Design

We are a consultancy to help builders to optimize their planning in order to save building costs. For that reason we need a website to offer our services, present our history, the mission and offer a plug-in for a first contact (including calendar), testimonials, a blog etc.
As an idea, I really like: https://www.fendrowadvisory.de/
Later on the website should be programmed in www.quelvo.de in our Wordpress area. The text, of course, will be done by myself. The colors should be suitable to our recently designed logo.

```html
<!DOCTYPE html>
<html lang="en">
<head>
<meta charset="utf-8">
<title>Tarvik Plans</title>
<link href="https://fonts.googleapis.com/css2?family=Inter:wght@400;500;600;700;800&display=swap" rel="stylesheet">
<style>
:root{
  --brand:#BE7E2C;
  --brand-light:#D9A25A;
  --ink:#111111;
  --text:#333333;
  --muted:#8a8a8a;
  --grey:#EDEDED;
  --soft:#F2F2F2;
  --line:#E4C9A4;
  --dark:#1E1E1E;
  --white:#ffffff;
}
*{margin:0;padding:0;box-sizing:border-box}
html,body{width:1200px;height:3813px;overflow:hidden}
body{position:relative;font-family:'Inter',sans-serif;color:var(--text);background:var(--white)}
.abs{position:absolute}
.photo{position:absolute;background:linear-gradient(135deg,#8c7a66,#c9b8a2 55%,#6f6253)}
.label{position:absolute;font-size:11px;font-weight:600;color:var(--brand)}
.h2{position:absolute;font-weight:800;color:var(--ink);font-size:42px;letter-spacing:-.5px}
.para{position:absolute;font-size:11.5px;line-height:18.7px;color:var(--text)}
.pill{position:absolute;height:40px;border-radius:20px;background:var(--brand);color:#fff;font-size:11.5px;font-weight:700;display:flex;align-items:center;padding-left:27px}
.pill .dot{position:absolute;right:-6px;top:9px;width:22px;height:22px;border-radius:50%;border:1.5px solid var(--brand);background:#fff;display:flex;align-items:center;justify-content:center}
.hero-grey{left:873px;top:0;width:327px;height:750px;background:var(--grey)}
.brand{left:188px;top:30px;display:flex;align-items:center;gap:8px;color:#fff;font-weight:700;font-size:17px}
.brand .mark{width:28px;height:28px;border:2px solid #fff}
.nav{top:37px;font-size:11.5px;color:#fff}
.contact-btn{left:894px;top:27px;width:118px;height:35px;border-radius:18px;background:var(--brand);color:#fff;font-weight:700;font-size:12.5px;display:flex;align-items:center;justify-content:center}
.badge{left:188px;top:215px;width:325px;height:32px;border-radius:16px;background:#F5D98C;display:flex;align-items:center;padding:0 5px;font-size:10px;color:#222;gap:12px}
.badge b{background:var(--brand);color:#fff;border-radius:12px;padding:5px 16px;font-size:10px}
.hero-title{left:188px;top:258px;font-size:42px;line-height:48px;font-weight:800;color:#fff}
.hero-text{left:188px;top:366px;width:345px;font-size:11px;line-height:18.5px;color:#fff}
.booking{left:188px;top:469px;width:472px;height:62px;background:#fff;border-radius:8px;border:2px solid #F3E2C8;display:flex;align-items:center;font-size:11px;color:#555}
.booking .f{display:flex;align-items:center;gap:7px;padding-left:22px}
.booking .sep{width:1px;height:30px;background:#ddd;margin-left:52px}
.booking .go{position:absolute;right:6px;top:6px;width:68px;height:46px;border-radius:6px;background:var(--brand);display:flex;align-items:center;justify-content:center}
.hero-photo{left:595px;top:133px;width:549px;height:542px;border-radius:50% 0 50% 50%}
.play{left:148px;top:959px;width:80px;height:80px;border-radius:50%;background:var(--brand);display:flex;align-items:center;justify-content:center}
.play-ring{left:138px;top:949px;width:100px;height:100px;border-radius:50%;border:1.5px dashed var(--brand-light)}
.card{position:absolute;width:203px;height:186px;border:1.5px solid var(--line);border-radius:4px;background:#fff;padding:18px 20px}
.card.active{background:var(--brand);border-color:var(--brand)}
.card .ico{width:34px;height:34px;border-radius:4px;background:#efefef;margin-bottom:14px;display:flex;align-items:center;justify-content:center}
.card.active .ico{background:#F5D98C}
.card h3{font-size:12px;font-weight:700;color:var(--ink);line-height:15px;margin-bottom:6px}
.card p{font-size:9.5px;line-height:13px;color:var(--muted);width:140px}
.card a{position:absolute;left:20px;bottom:20px;font-size:8.5px;color:var(--brand);text-decoration:underline}
.card.active h3,.card.active p,.card.active a{color:#fff}
.testi-bg{left:0;top:1761px;width:1200px;height:644px;background:var(--soft)}
.testi-panel{left:0;top:1804px;width:380px;height:558px;background:var(--brand);border-radius:0 18px 18px 0}
.arrow-btn{position:absolute;width:28px;height:28px;border-radius:50%;border:1.5px solid var(--brand);background:#fff;display:flex;align-items:center;justify-content:center}
.news{position:absolute;top:2560px;width:262px;height:349px;border:1.5px solid var(--line);border-radius:12px;background:#fff}
.news .img{position:absolute;left:8px;top:0;width:246px;height:182px;border-radius:10px;background:linear-gradient(135deg,#6f7a86,#b9c2c9 60%,#5d6670)}
.news .date{position:absolute;left:20px;top:203px;font-size:11px;color:var(--brand);display:flex;gap:6px;align-items:center}
.news h3{position:absolute;left:20px;top:229px;width:230px;font-size:13px;line-height:16px;font-weight:700;color:var(--ink)}
.news p{position:absolute;left:20px;top:270px;width:210px;font-size:9.5px;line-height:14px;color:#444}
.news .more{position:absolute;left:20px;top:312px;font-size:11.5px;font-weight:700;color:var(--brand)}
.side-arrow{position:absolute;top:2731px;width:28px;height:28px;border-radius:50%;border:1.5px solid #bbb;display:flex;align-items:center;justify-content:center}
.field{position:absolute;height:52px;border:1.5px solid #ddd;border-radius:4px;background:#fff;font-size:11.5px;color:#333;padding:0 18px;display:flex;align-items:center;justify-content:space-between}
.footer{left:0;top:3452px;width:1200px;height:361px;background:var(--dark)}
.foot-h{position:absolute;top:3521px;font-size:13px;font-weight:700;color:#fff;letter-spacing:.5px}
.foot-list{position:absolute;top:3556px;list-style:none;font-size:10.5px;color:#aaa}
.foot-list li{height:24.5px}
.foot-list li::before{content:"›";color:var(--brand);margin-right:6px}
.social{position:absolute;top:3586px;width:28px;height:28px;border-radius:50%;background:#3a3a3a}
.news-input{left:841px;top:3555px;width:168px;height:36px;border-radius:18px;background:#fff;font-size:8.5px;color:#777;display:flex;align-items:center;padding-left:12px}
.news-input .go{position:absolute;right:0;top:0;width:36px;height:36px;border-radius:50%;background:var(--brand);display:flex;align-items:center;justify-content:center}
.foot-rule{left:0;top:3766px;width:1200px;height:1px;background:#333}
.foot-small{top:3783px;font-size:10px;color:#aaa}
</style>
</head>
<body>

<div class="abs hero-grey"></div>
<svg class="abs" style="left:0;top:0" width="1200" height="812" viewBox="0 0 1200 812">
  <path d="M0 0 H873 V300 C873 600 640 811 330 811 H0 Z" fill="#BE7E2C"/>
</svg>
<div class="photo hero-photo" role="img" aria-label="Two construction workers in hard hats reviewing plans on a building site"></div>

<div class="abs brand"><span class="mark"></span>Tarvik Plans</div>
<div class="abs nav" style="left:465px">Home</div>
<div class="abs nav" style="left:537px">Services</div>
<div class="abs nav" style="left:624px">About us</div>
<div class="abs nav" style="left:716px">Testimonials</div>
<div class="abs nav" style="left:823px">Blog</div>
<div class="abs contact-btn">Contact us</div>

<div class="abs badge"><b>NEW</b>Get the latest update of coronavirus (COVID-19)</div>
<h1 class="abs hero-title">Protecting you<br>and you family</h1>
<p class="abs hero-text">when an unknown printer took a galley of type and scrambled it to make a type specimen book. It has survived not only five centuries, but also the leap into electronic typesetting, remaining essentially unchanged.</p>
<div class="abs booking">
  <span class="f"><svg width="13" height="13" viewBox="0 0 14 14" fill="none" stroke="#666" stroke-width="1.2"><rect x="1.5" y="2.5" width="11" height="10" rx="1.5"/><path d="M1.5 6h11M4.5 1v3M9.5 1v3"/></svg>Select A Day</span>
  <span class="sep"></span>
  <span class="f" style="padding-left:42px"><svg width="13" height="13" viewBox="0 0 14 14" fill="none" stroke="#666" stroke-width="1.2"><circle cx="7" cy="7" r="5.5"/><path d="M7 4v3.2l2 1.5"/></svg>Select An Hour</span>
  <span class="go"><svg width="24" height="20" viewBox="0 0 24 20"><path d="M2 2 L22 10 L2 18 L6 10 Z" fill="#fff"/></svg></span>
</div>

<div class="photo" style="left:188px;top:873px;width:361px;height:348px;border-radius:8px" role="img" aria-label="Engineer and architect studying a large blueprint on site"></div>
<div class="photo" style="left:444px;top:1098px;width:141px;height:141px;border:4px solid #fff;background:linear-gradient(135deg,#4f7ea3,#c9a35e 60%,#e07b2b)" role="img" aria-label="Workers in safety vests discussing plans"></div>
<div class="abs play-ring"></div>
<div class="abs play"><svg width="20" height="22" viewBox="0 0 20 22"><path d="M3 2 L18 11 L3 20 Z" fill="#fff"/></svg></div>
<div class="label" style="left:627px;top:889px">ABOUT</div>
<h2 class="h2" style="left:627px;top:905px">ABOUT US</h2>
<p class="para" style="left:627px;top:965px;width:388px">It is a long established fact that a reader will be distracted by the readable content of a page when looking at its layout. The point of using Lorem Ipsum is that it has a more-or-less normal distribution of letters, opposed to using 'Content here, content here', making it look like English. Many desktop publishing packages and web page editors now use Lorem Ipsum as their default model text, and a search for 'lorem ipsum' will uncover many web sites still in their infancy. Various versions have evolved over the years, sometimes by accident, sometimes on purpose (injected humour and the like).</p>
<div class="pill" style="left:627px;top:1161px;width:126px">READ MORE<span class="dot"><svg width="10" height="10" viewBox="0 0 10 10" fill="none" stroke="#BE7E2C" stroke-width="1.4"><path d="M1 5h8M6 2l3 3-3 3"/></svg></span></div>

<div class="label" style="left:188px;top:1410px">SERVICE</div>
<h2 class="h2" style="left:188px;top:1424px">Our Service</h2>
<p class="para" style="left:188px;top:1484px;width:352px">It is a long established fact that a reader will be distracted by the readable content of a page when looking at its layout. The point of using Lorem Ipsum is that it has a more-or-less.</p>
<div class="pill" style="left:188px;top:1560px;width:126px">READ MORE<span class="dot"><svg width="10" height="10" viewBox="0 0 10 10" fill="none" stroke="#BE7E2C" stroke-width="1.4"><path d="M1 5h8M6 2l3 3-3 3"/></svg></span></div>

<div class="card active" style="left:593px;top:1308px">
  <div class="ico"><svg width="22" height="22" viewBox="0 0 22 22" fill="none" stroke="#BE7E2C" stroke-width="1.4"><rect x="2" y="2" width="18" height="18" rx="1"/><path d="M6 16l9-9M13 6l3 3M5 8h5M5 11h3"/></svg></div>
  <h3>Construction Planning and Design</h3>
  <p>Lorem Ipsum is simply dummy text of the printing and typesetting industry.</p>
  <a>Learn more</a>
</div>
<div class="card" style="left:811px;top:1308px">
  <div class="ico"><svg width="22" height="22" viewBox="0 0 22 22" fill="none" stroke="#333" stroke-width="1.4"><rect x="3" y="2" width="16" height="18" rx="1"/><rect x="6" y="5" width="10" height="4"/><path d="M6 12h2M10 12h2M14 12h2M6 16h2M10 16h2M14 16h2"/></svg></div>
  <h3>Cost Estimation and Budgeting</h3>
  <p>Lorem Ipsum is simply dummy text of the printing and typesetting industry.</p>
  <a>Learn more</a>
</div>
<div class="card" style="left:593px;top:1509px">
  <div class="ico"><svg width="22" height="22" viewBox="0 0 22 22" fill="none" stroke="#333" stroke-width="1.4"><path d="M3 19h16M5 19v-5M9 19v-8M13 19v-6M17 19v-11"/><circle cx="7" cy="6" r="3"/></svg></div>
  <h3>Value Engineering and Value Management</h3>
  <p>Lorem Ipsum is simply dummy text of the printing and typesetting industry.</p>
  <a>Learn more</a>
</div>
<div class="card" style="left:811px;top:1509px">
  <div class="ico"><svg width="22" height="22" viewBox="0 0 22 22" fill="none" stroke="#333" stroke-width="1.4"><rect x="2" y="4" width="18" height="15" rx="1"/><path d="M6 19V8h4v11M12 19V10h4v9"/></svg></div>
  <h3>Construction Project Management</h3>
  <p>Lorem Ipsum is simply dummy text of the printing and typesetting industry.</p>
  <a>Learn more</a>
</div>

<div class="abs testi-bg"></div>
<div class="abs testi-panel"></div>
<div class="photo" style="left:212px;top:1863px;width:355px;height:441px;border-radius:10px;background:linear-gradient(160deg,#d8d4cc,#8a9070 55%,#3f4a36)" role="img" aria-label="Smiling businesswoman in glasses giving a thumbs up"></div>
<div class="label" style="left:651px;top:1904px">Testimonials</div>
<h2 class="h2" style="left:651px;top:1918px">Customer reviews</h2>
<svg class="abs" style="left:651px;top:1980px" width="40" height="34" viewBox="0 0 40 34"><path d="M2 34V20C2 9 7 3 16 0l2 4c-5 2-8 6-8 12h8v18ZM22 34V20c0-11 5-17 14-20l2 4c-5 2-8 6-8 12h8v18Z" fill="#BE7E2C"/></svg>
<p class="para" style="left:651px;top:2043px;width:370px">It is a long established fact that a reader will be distracted by the an readable content of a page when looking at its layout. The point of using Lorem Ipsum is that it has a more-or-less normal distribution of letters,opposed to using 'Content here, content here', making it look like&nbsp; English.</p>
<div class="abs" style="left:651px;top:2185px;font-size:11.5px;color:#222">Lena Hartwig, Senior Consultant</div>
<div class="arrow-btn" style="left:651px;top:2232px"><svg width="10" height="10" viewBox="0 0 10 10"><path d="M7 1L2 5l5 4z" fill="#BE7E2C"/></svg></div>
<div class="arrow-btn" style="left:687px;top:2232px"><svg width="10" height="10" viewBox="0 0 10 10"><path d="M3 1l5 4-5 4z" fill="#BE7E2C"/></svg></div>

<div class="label" style="left:0;width:1200px;text-align:center;top:2465px">News</div>
<h2 class="h2" style="left:0;width:1200px;text-align:center;top:2480px">Latest News</h2>
<div class="side-arrow" style="left:138px"><svg width="12" height="12" viewBox="0 0 12 12" fill="none" stroke="#999" stroke-width="1.3"><path d="M11 6H2M5 3L2 6l3 3"/></svg></div>
<div class="side-arrow" style="left:1032px;border-color:var(--brand)"><svg width="12" height="12" viewBox="0 0 12 12" fill="none" stroke="#BE7E2C" stroke-width="1.3"><path d="M1 6h9M7 3l3 3-3 3"/></svg></div>

<div class="news" style="left:188px">
  <div class="img" role="img" aria-label="Two colleagues talking in a modern office"></div>
  <div class="date"><svg width="11" height="11" viewBox="0 0 12 12" fill="none" stroke="#BE7E2C" stroke-width="1.2"><circle cx="6" cy="6" r="5"/><path d="M6 3v3l2 1.5"/></svg>11 July 2023</div>
  <h3>Perspiciatis unde omnis is natus voluptatem doloremque</h3>
  <p>Lorem Ipsum is simply dummy text. of the printing and typesetting.</p>
  <div class="more">Read More →</div>
</div>
<div class="news" style="left:469px">
  <div class="img" role="img" aria-label="Team meeting around a table"></div>
  <div class="date"><svg width="11" height="11" viewBox="0 0 12 12" fill="none" stroke="#BE7E2C" stroke-width="1.2"><circle cx="6" cy="6" r="5"/><path d="M6 3v3l2 1.5"/></svg>11 July 2023</div>
  <h3>Perspiciatis unde omnis is natus voluptatem doloremque</h3>
  <p>Lorem Ipsum is simply dummy text. of the printing and typesetting.</p>
  <div class="more">Read More →</div>
</div>
<div class="news" style="left:750px">
  <div class="img" role="img" aria-label="Colleagues reviewing work on a laptop"></div>
  <div class="date"><svg width="11" height="11" viewBox="0 0 12 12" fill="none" stroke="#BE7E2C" stroke-width="1.2"><circle cx="6" cy="6" r="5"/><path d="M6 3v3l2 1.5"/></svg>11 July 2023</div>
  <h3>Perspiciatis unde omnis is natus voluptatem doloremque</h3>
  <p>Lorem Ipsum is simply dummy text. of the printing and typesetting.</p>
  <div class="more">Read More →</div>
</div>

<div class="label" style="left:0;width:1200px;text-align:center;top:2971px">Contact Us</div>
<h2 class="h2" style="left:0;width:1200px;text-align:center;top:2986px">Get In Touch</h2>
<div class="field" style="left:188px;top:3065px;width:402px">Name<svg width="13" height="13" viewBox="0 0 14 14" fill="#BE7E2C"><circle cx="7" cy="4" r="3"/><path d="M1 14c0-4 3-6 6-6s6 2 6 6z"/></svg></div>
<div class="field" style="left:610px;top:3065px;width:402px">Email<svg width="14" height="11" viewBox="0 0 14 11" fill="#BE7E2C"><rect width="14" height="11" rx="1"/><path d="M1 1l6 5 6-5" stroke="#fff" fill="none"/></svg></div>
<div class="field" style="left:188px;top:3134px;width:402px">Phone<svg width="13" height="13" viewBox="0 0 14 14" fill="#BE7E2C"><path d="M3 1l3 3-2 2c1 2 2 3 4 4l2-2 3 3-2 2C6 13 1 8 1 3z"/></svg></div>
<div class="field" style="left:610px;top:3134px;width:402px">Subject<svg width="13" height="13" viewBox="0 0 14 14" fill="none" stroke="#BE7E2C" stroke-width="1.3"><path d="M12 8v5H1V2h5M6 9l1-3 5-5 2 2-5 5z"/></svg></div>
<div class="field" style="left:188px;top:3205px;width:824px;height:184px;align-items:flex-start;padding-top:18px">Message Here<svg width="13" height="13" viewBox="0 0 14 14" fill="none" stroke="#BE7E2C" stroke-width="1.3"><path d="M12 8v5H1V2h5M6 9l1-3 5-5 2 2-5 5z"/></svg></div>
<div class="pill" style="left:861px;top:3330px;width:126px;font-weight:600">Submit Now<span class="dot"><svg width="10" height="10" viewBox="0 0 10 10" fill="none" stroke="#BE7E2C" stroke-width="1.4"><path d="M1 5h8M6 2l3 3-3 3"/></svg></span></div>

<div class="abs footer"></div>
<div class="abs" style="left:188px;top:3530px;font-size:17px;font-weight:700;color:var(--brand)">Tarvik Plans</div>
<div class="social" style="left:205px"></div>
<div class="social" style="left:240px"></div>
<div class="social" style="left:275px"></div>

<div class="foot-h" style="left:377px">Quick Links</div>
<ul class="foot-list" style="left:377px"><li>Home</li><li>About Us</li><li>Services</li><li>Testimonials</li><li>Contact Us</li></ul>

<div class="foot-h" style="left:534px">Contact</div>
<div class="abs" style="left:534px;top:3556px;font-size:10.5px;line-height:18px;color:#aaa">
  <span style="color:var(--brand)">◈</span>&nbsp; 418 Marlow Lane<br>Eastfield, OH 44012
</div>
<div class="abs" style="left:534px;top:3606px;font-size:10.5px;color:#aaa"><span style="color:var(--brand)">▮</span>&nbsp; 284-615-0397</div>
<div class="abs" style="left:534px;top:3640px;font-size:10.5px;color:#aaa"><span style="color:var(--brand)">✉</span>&nbsp; info@tarvikplans</div>

<div class="foot-h" style="left:709px">Company</div>
<ul class="foot-list" style="left:709px"><li>Lorem Ipsum</li><li>Lorem Ipsum</li><li>Lorem Ipsum</li><li>Lorem Ipsum</li><li>Lorem Ipsum</li></ul>

<div class="foot-h" style="left:841px">Subscribe Our Newsletter</div>
<div class="abs news-input">Enter Email Address<span class="go"><svg width="12" height="12" viewBox="0 0 12 12" fill="none" stroke="#fff" stroke-width="1.5"><path d="M1 6h10M7 2l4 4-4 4"/></svg></span></div>

<div class="abs foot-rule"></div>
<div class="abs foot-small" style="left:184px">© Tarvik Plans. All Rights Reserved</div>
<div class="abs foot-small" style="left:804px">Terms &amp; Conditions</div>
<div class="abs foot-small" style="left:920px;color:#555">|</div>
<div class="abs foot-small" style="left:944px">Privacy Policy</div>

</body>
</html>
```